New Business Card Design Project

2 sided business card required. I have attached some previous designs of items we have had made so you can see the logo etc. we Want the card to look professional and modern. for the final design upload for winning designer please note I need to be able to edit the names / phone numbers on the card design as I need to get them made for different staff.
Updates

extending time so designers can have time to submit

Target Market(s)

new customers

Industry/Entity Type

transport / earthmoving

Contact Information for Business Card

name, phone number email address

Requirements
Nice to have
• professional / impressive looking card (first impressions to customers count)
Should not have
• do not put our mobile number on the design use a generic number

```html
<!DOCTYPE html>
<html lang="en">
<head>
<meta charset="utf-8">
<title>RPH Pty Ltd – Business Card</title>
<link href="https://fonts.googleapis.com/css2?family=Roboto:wght@400;500;700;900&family=Roboto+Condensed:wght@400;700&display=swap" rel="stylesheet">
<style>
  :root{
    --page:#5b5b5d;
    --card-black:#0d0d0d;
    --panel-dark:#1c1c1e;
    --tan:#d49a68;
    --tan-dark:#b97c4b;
    --earth:#a0643a;
    --sky-dark:#1a1a1c;
    --white:#ffffff;
    --silver-light:#e6e6e6;
    --silver-dark:#9a9a9a;
    --grey-label:#8c8c8c;
    --text-dark:#141414;
  }
  *{box-sizing:border-box;margin:0;padding:0}
  html,body{width:1200px;height:924px;overflow:hidden}
  body{background:var(--page);font-family:"Roboto",Arial,sans-serif;position:relative}

  .card{position:absolute;left:280px;width:640px;height:366px;background:var(--card-black);overflow:hidden;box-shadow:0 10px 24px rgba(0,0,0,.35)}
  .card--front{top:60px}
  .card--back{top:498px}

  /* ---------- front ---------- */
  .texture-panel{position:absolute;left:0;top:0;width:330px;height:240px;
    background:radial-gradient(ellipse at 55% 40%,#3a3a3d 0%,#1b1b1d 55%,var(--card-black) 100%)}
  .haul-photo{position:absolute;left:230px;top:0;width:410px;height:250px;
    clip-path:polygon(25% 0,100% 0,100% 100%,0 100%);
    background:linear-gradient(180deg,var(--sky-dark) 0%,#2c2a28 35%,#6e4a2e 60%,var(--earth) 80%,var(--tan) 100%)}
  .brand{position:absolute;left:62px;top:60px;display:flex;align-items:flex-end;gap:10px;color:var(--silver-light);font-weight:900}
  .brand__name{font-size:86px;line-height:1;letter-spacing:2px}
  .brand__suffix{font-size:20px;margin-bottom:56px}

  .name-band{position:absolute;left:0;top:236px;width:300px;height:40px;background:var(--tan);
    clip-path:polygon(0 0,100% 0,93% 100%,0 100%);
    font-weight:900;font-size:26px;color:var(--text-dark);padding:4px 0 0 26px;letter-spacing:.5px}
  .person{position:absolute;left:26px;top:284px}
  .person__name{color:var(--white);font-weight:700;font-size:22px;letter-spacing:1px}
  .person__role{color:var(--tan);font-weight:700;font-size:14px;letter-spacing:1px;margin-top:2px}

  .contact-list{position:absolute;left:300px;top:208px;list-style:none}
  .contact-list li{display:flex;align-items:center;gap:10px;color:var(--white);height:26px;font-size:16px;font-weight:500}
  .contact-list li.phone{font-size:20px;font-weight:700}
  .contact-icon{width:22px;height:22px;flex:none}

  .depot-band{position:absolute;left:0;bottom:0;width:640px;height:38px;
    background:linear-gradient(180deg,var(--silver-light),var(--silver-dark));
    color:var(--text-dark);font-family:"Roboto Condensed",Arial,sans-serif;font-weight:700;font-size:18px;
    padding:8px 0 0 26px;letter-spacing:.5px}

  /* ---------- back ---------- */
  .machine-photo{position:absolute;left:0;top:0;width:330px;height:366px;
    background:radial-gradient(ellipse at 55% 65%,#8c6a4c 0%,#5a3d26 35%,#2a2320 65%,var(--card-black) 100%)}
  .card--back .brand{left:34px;top:34px}
  .card--back .brand__name{font-size:62px}
  .card--back .brand__suffix{font-size:16px;margin-bottom:40px}

  .services{position:absolute;left:318px;top:22px;width:310px}
  .services__title{display:inline-block;background:var(--grey-label);color:var(--text-dark);
    font-weight:900;font-size:17px;padding:2px 10px;letter-spacing:.5px}
  .services__list{list-style:none;margin-top:6px}
  .services__list li{position:relative;color:var(--white);font-size:13.5px;line-height:19px;padding-left:18px}
  .services__list li::before{content:"";position:absolute;left:2px;top:5px;width:9px;height:9px;border-radius:50%;
    background:var(--silver-light);box-shadow:inset 0 0 0 2px var(--silver-dark)}

  .quote-band{position:absolute;left:300px;bottom:0;width:340px;height:70px;background:var(--tan);
    clip-path:polygon(6% 0,100% 0,100% 100%,0 100%);
    color:var(--text-dark);font-weight:700;font-size:13px;line-height:17px;padding:9px 14px 0 36px}
</style>
</head>
<body>

<section class="card card--front" aria-label="Business card front">
  <div class="texture-panel" role="img" aria-label="Dark hexagonal metal mesh texture"></div>
  <div class="haul-photo" role="img" aria-label="Photo of a road train truck on red outback dirt at dusk"></div>

  <div class="brand">
    <span class="brand__name">RPH</span>
    <span class="brand__suffix">Pty Ltd</span>
  </div>

  <div class="name-band">RPH PTY LTD</div>
  <div class="person">
    <div class="person__name">DANIEL BROOKS</div>
    <div class="person__role">DIRECTOR</div>
  </div>

  <ul class="contact-list">
    <li class="phone">
      <svg class="contact-icon" viewBox="0 0 24 24"><circle cx="12" cy="12" r="11" fill="none" stroke="#e6e6e6" stroke-width="1.5"/><path d="M8 6.5l2 2.5-1.2 1.5a7 7 0 0 0 4.7 4.7L15 14l2.5 2-1 2C11 18 6 13 6 7.5z" fill="#e6e6e6"/></svg>
      098 765 4321
    </li>
    <li>
      <svg class="contact-icon" viewBox="0 0 24 24"><circle cx="12" cy="12" r="11" fill="none" stroke="#e6e6e6" stroke-width="1.5"/><rect x="6" y="8" width="12" height="8" fill="none" stroke="#e6e6e6" stroke-width="1.5"/><path d="M6 8l6 5 6-5" fill="none" stroke="#e6e6e6" stroke-width="1.5"/></svg>
      accounts@redplainhaulage.com.au
    </li>
    <li>
      <svg class="contact-icon" viewBox="0 0 24 24"><circle cx="12" cy="12" r="11" fill="none" stroke="#e6e6e6" stroke-width="1.5"/><circle cx="12" cy="12" r="6" fill="none" stroke="#e6e6e6" stroke-width="1.3"/><path d="M6 12h12M12 6c-3 3-3 9 0 12M12 6c3 3 3 9 0 12" fill="none" stroke="#e6e6e6" stroke-width="1.1"/></svg>
      www.redplainhaulage.com.au
    </li>
  </ul>

  <div class="depot-band">DEPOT: LOT 46, GIBBER FLAT ROAD MARLA RIDGE, AUSTRALIA</div>
</section>

<section class="card card--back" aria-label="Business card back">
  <div class="machine-photo" role="img" aria-label="Photo of a skid steer loader moving red earth"></div>

  <div class="brand">
    <span class="brand__name">RPH</span>
    <span class="brand__suffix">Pty Ltd</span>
  </div>

  <div class="services">
    <span class="services__title">OUR SERVICES</span>
    <ul class="services__list">
      <li>Over size loads / Hot Shot Loads</li>
      <li>Heavy Vehicle Recovery services</li>
      <li>Potable Water Deliveries</li>
      <li>Road Building / Maintenance</li>
      <li>Earthworks</li>
      <li>Sand &amp; Metal Supply &amp; Cartage</li>
      <li>Road Train Tippers</li>
      <li>Road Train Tankers</li>
      <li>Road Train Flat Tops</li>
      <li>Drop Deck Trailers</li>
      <li>Mine site accredited equipment &amp; Operators</li>
    </ul>
  </div>

  <div class="quote-band">We offer a large range of services not listed so call us today for a personalised quote to suit your needs.</div>
</section>

</body>
</html>
```